Letterhead Design Project

We have recently updated our corporate logo and are seeking a new letterhead template.

Attached is the new logo and the old letterhead.

PLEASE DO NOT USE OUR EXISTING WEB SITE FOR INSPIRATION as we are redesigning it.

Target Market(s)

Executives, search professionals, technical and scientific professionals

Industry/Entity Type

Seeking

```html
<!DOCTYPE html>
<html lang="en">
<head>
<meta charset="utf-8">
<title>Verlane Labs Letterhead</title>
<link rel="stylesheet" href="https://fonts.googleapis.com/css2?family=Open+Sans:wght@400;600&display=swap">
<style>
  :root {
    --brand-blue: #1b90cc;
    --brand-slate: #5a6064;
    --decor-grey: #ebebed;
    --paper: #ffffff;
    --footer-text: #ffffff;
  }
  * { margin: 0; padding: 0; box-sizing: border-box; }
  html, body {
    width: 927px;
    height: 1200px;
    overflow: hidden;
    background: var(--paper);
  }
  .letterhead {
    position: relative;
    width: 927px;
    height: 1200px;
    overflow: hidden;
    background: var(--paper);
    font-family: "Open Sans", Arial, sans-serif;
  }
  .corner-decor {
    position: absolute;
    top: 0;
    right: 0;
    width: 290px;
    height: 295px;
  }
  .brand-name {
    position: absolute;
    top: 36px;
    left: 27px;
    font-weight: 600;
    font-size: 36px;
    line-height: 1;
    color: var(--brand-slate);
  }
  .web-address {
    position: absolute;
    top: 60px;
    left: 698px;
    font-size: 15px;
    color: var(--brand-blue);
  }
  .footer-band {
    position: absolute;
    left: 0;
    bottom: 0;
    width: 927px;
    height: 85px;
    background: linear-gradient(90deg, var(--brand-blue) 0%, #3f8bbd 40%, #63666c 100%);
    display: flex;
    flex-direction: column;
    align-items: center;
    justify-content: center;
    color: var(--footer-text);
    font-size: 14px;
    line-height: 20px;
    text-align: center;
  }
</style>
</head>
<body>
  <main class="letterhead">
    <svg class="corner-decor" viewBox="0 0 290 295" aria-hidden="true">
      <circle cx="290" cy="5" r="290" fill="var(--decor-grey)"/>
    </svg>

    <header>
      <p class="brand-name">Verlane Labs</p>
    </header>

    <p class="web-address">www.verlanelabs.com</p>

    <footer class="footer-band">
      <p class="footer-address">2400 North Ridge Road, Suite 410&nbsp; •&nbsp; Brookfield, MA 01506</p>
      <p class="footer-contact">Phone 508.555.0140 • Fax 508.555.0150</p>
    </footer>
  </main>
</body>
</html>
```